Brisvale services brochure

We need a new company brochure. The brochure will be formatted for PDF distribution but should be printable on "letter" size paper. 2 pages plus front and back cover. Color white and same blue as logo. Logo "O" should be used as design. Look at webpage for general info: www.brisvale.ca<br/><br/>Front cover: pic1, logo, design and "Your Cleaning is Our Business". <br/>Back cover" "O" design, logo and info from "contact" page<br/>Front cover inside: design and intro from web home page, also use stock pics of clean offices ect as placeholders for purchased pics.<br/>1st page: design and "Our Services", use info of "Cleanroom & GMP Services", "Janitorial Services" from services page.<br/>2nd page: design and "Special Services", info from "Carpet & Upholstery Services", "Window Cleaning Services", and list of "Other Services".<br/>Back cover inside : design and info from technology page, use stock pics for place holders.

Industry/Entity Type

Janitorial

Font styles to use
Sans Serif
Other font styles liked:
• Futura Book

Colors
0555a3

Requirements
Must have
• The logo "O" (target) should be part of the design. Design color same as logo.

```html
<!DOCTYPE html>
<html lang="en">
<head>
<meta charset="utf-8">
<title>Brisvale Building Services Brochure</title>
<link href="https://fonts.googleapis.com/css2?family=Jost:wght@400&family=Roboto:wght@400;500;700&family=Roboto+Condensed:wght@400&display=swap" rel="stylesheet">
<style>
:root{
  --brand:#0555a3;
  --brand-mid:#1b75c4;
  --navy:#1b2a6b;
  --ink:#4a4a4a;
  --grey:#5d5f63;
  --paper:#ffffff;
  --backdrop:#d7d8da;
}
*{margin:0;padding:0;box-sizing:border-box}
html,body{width:886px;height:1200px;overflow:hidden;background:var(--backdrop)}
body{font-family:"Roboto",Arial,sans-serif;color:var(--ink);position:relative}
.spread{position:absolute;left:45px;width:796px;height:514px;display:flex}
.spread--inside{top:44px}
.spread--cover{top:598px}
.page{position:relative;width:398px;height:514px;background:var(--paper);overflow:hidden}
.abs{position:absolute}
.wordmark{font-family:"Jost",sans-serif;font-weight:400;color:var(--brand);letter-spacing:4px;line-height:1;white-space:nowrap;display:flex;align-items:center;gap:8px}
.wordmark__dot{width:7px;height:7px;background:var(--brand);border-radius:50%}
.section-title{color:var(--brand-mid);font-size:13.5px;font-weight:400;letter-spacing:-.2px}
.body-copy{font-size:8.4px;line-height:11.7px;text-align:justify;color:var(--ink)}
.feature{position:absolute;width:150px}
.feature__icon{position:absolute;left:-28px;top:-2px;width:23px;height:23px}
.feature__title{color:var(--brand-mid);font-size:8.6px;margin-bottom:2px}
.feature__text{font-size:7px;line-height:11px;text-align:justify;color:var(--ink)}
.availability{width:398px;text-align:center;color:var(--brand-mid);font-size:9.2px}
.slogan{width:398px;text-align:center;color:var(--brand-mid);font-size:11px}
.contact-bar{left:0;top:477px;width:350px;height:18px;background:var(--brand-mid);clip-path:polygon(0 0,94% 0,100% 100%,0 100%);display:flex;align-items:center;gap:0;padding-left:23px;color:#fff;font-size:7.2px;font-weight:700}
.contact-bar span{display:flex;align-items:center;gap:3px}
.contact-bar svg{width:7px;height:7px}
.headline{width:398px;text-align:center;color:var(--grey);font-size:18.5px;line-height:22px;letter-spacing:.3px}
.values{list-style:none;font-size:8.4px;color:var(--grey);letter-spacing:.2px}
.values li{display:flex;align-items:center;gap:6px;height:15.5px}
.values svg{width:8px;height:8px}
.offers{display:flex;gap:3px}
.offer{width:44px;height:44px;background:var(--brand-mid);border-radius:5px;color:#fff;font-size:5.6px;line-height:7px;text-align:center;display:flex;flex-direction:column;justify-content:center;box-shadow:0 2px 2px rgba(0,0,0,.25)}
.offer small{font-size:4.2px;line-height:5px}
.other-list{display:grid;grid-template-columns:162px 190px;column-gap:0}
.other-list div{display:flex;align-items:center;gap:7px;height:24.3px;border-bottom:1px solid #ececec;font-family:"Roboto Condensed",sans-serif;font-size:9px;color:var(--grey)}
.other-list svg{width:9px;height:9px;flex:none}
.band{left:0;top:298px;width:398px;height:216px;background:linear-gradient(135deg,#1f5fae 0%,var(--navy) 100%)}
.band-title{color:#fff;font-size:10px}
.service{position:absolute;color:#fff}
.service__icon{position:absolute;width:32px;height:30px;border-radius:4px;background:rgba(255,255,255,.22)}
.service__title{font-size:6px;font-weight:700;margin-bottom:4px}
.service__text{font-size:5.8px;line-height:7px;width:125px;color:#e6ecf7}
.divider{left:199px;top:330px;height:170px;border-left:1px dashed rgba(255,255,255,.35)}
</style>
</head>
<body>
<svg width="0" height="0" style="position:absolute" aria-hidden="true">
  <symbol id="tick-circle" viewBox="0 0 20 20"><circle cx="10" cy="10" r="8.5" fill="none" stroke="currentColor" stroke-width="2"/><path d="M6 10.3l2.8 2.8L14.2 7.5" fill="none" stroke="currentColor" stroke-width="2"/></symbol>
  <symbol id="tick-box" viewBox="0 0 20 20"><rect x="2" y="4" width="14" height="14" fill="none" stroke="currentColor" stroke-width="2"/><path d="M6 10l3.5 3.5L18 3" fill="none" stroke="currentColor" stroke-width="2.2"/></symbol>
</svg>

<!-- Inside spread: technology page + front cover -->
<section class="spread spread--inside">
  <article class="page page--technology">
    <div class="abs wordmark" style="left:0;width:398px;justify-content:center;top:122px;font-size:27px"><i class="wordmark__dot"></i>BRISVALE</div>
    <h2 class="abs section-title" style="left:23px;top:157px">Quality Control System</h2>
    <p class="abs body-copy" style="left:24px;top:179px;width:359px">Brisvale supports a real time interactive system that monitors and manages customer satisfaction, providing its customers with the tools to control their customised services. Through the Brisvale online web based system, our customers have access and control of the following:</p>

    <div class="feature" style="left:51px;top:259px">
      <svg class="feature__icon" viewBox="0 0 24 24"><circle cx="12" cy="12" r="11" fill="var(--brand-mid)"/><rect x="8" y="6" width="8" height="12" fill="none" stroke="#fff" stroke-width="1"/><path d="M9.5 9h5M9.5 11.5h5M9.5 14h5" stroke="#fff" stroke-width=".8"/></svg>
      <div class="feature__title">Inspections</div>
      <div class="feature__text">Track trends to improve service, Perform detailed inspections, Track job performance, Correct deficiencies.</div>
    </div>
    <div class="feature" style="left:231px;top:259px">
      <svg class="feature__icon" viewBox="0 0 24 24"><circle cx="12" cy="12" r="11" fill="var(--brand-mid)"/><circle cx="12" cy="12" r="5.5" fill="none" stroke="#fff" stroke-width="1"/><path d="M12 9v3.3h2.5" fill="none" stroke="#fff" stroke-width="1"/></svg>
      <div class="feature__title">Job Scheduling</div>
      <div class="feature__text">Track compliance to contract specifications, Customize schedules to customer needs</div>
    </div>
    <div class="feature" style="left:51px;top:328px">
      <svg class="feature__icon" viewBox="0 0 24 24"><circle cx="12" cy="12" r="11" fill="var(--brand-mid)"/><rect x="7.5" y="6" width="8" height="12" fill="none" stroke="#fff" stroke-width="1"/><path d="M9 9.5h5M9 12h5M15 16l2.5-5" stroke="#fff" stroke-width=".9"/></svg>
      <div class="feature__title">Work order management</div>
      <div class="feature__text">Instantly distribute work orders to those responsible, Automatically escalate work orders to management.</div>
    </div>
    <div class="feature" style="left:231px;top:328px">
      <svg class="feature__icon" viewBox="0 0 24 24"><circle cx="12" cy="12" r="11" fill="var(--brand-mid)"/><rect x="8" y="6" width="8" height="12" fill="none" stroke="#fff" stroke-width="1"/><path d="M9.5 10h5M9.5 12.5h5M9.5 15h3" stroke="#fff" stroke-width=".8"/></svg>
      <div class="feature__title">Reports</div>
      <div class="feature__text">Address employee issues found during an inspection Outline services that need specific treatment.</div>
    </div>

    <p class="abs availability" style="left:0;top:426px">At Brisvale we are are available 24/7 for supporting our clients.</p>
    <p class="abs slogan" style="left:0;top:444px">“Your Cleaning is Our Business!”</p>

    <div class="abs contact-bar">
      <span style="width:117px"><svg viewBox="0 0 10 10"><circle cx="5" cy="5" r="4.3" fill="none" stroke="#fff"/><path d="M3 4l2 1.5L7 4" fill="none" stroke="#fff" stroke-width=".8"/></svg>info@brisvale.ca</span>
      <span style="width:107px"><svg viewBox="0 0 10 10"><path d="M2.5 1.5l2 2-1 1c.5 1 1.2 1.7 2 2l1-1 2 2-1.3 1.3C4.5 8.5 1.5 5.5 1.2 2.8z" fill="none" stroke="#fff" stroke-width=".8"/></svg>1 (800) 555-0142</span>
      <span><svg viewBox="0 0 10 10"><circle cx="5" cy="5" r="4.3" fill="none" stroke="#fff"/><path d="M1 5h8M5 1c-2 2.5-2 5.5 0 8M5 1c2 2.5 2 5.5 0 8" fill="none" stroke="#fff" stroke-width=".6"/></svg>www.brisvale.ca</span>
    </div>
  </article>

  <article class="page page--front">
    <div class="abs wordmark" style="left:0;width:398px;justify-content:center;top:54px;font-size:30px"><i class="wordmark__dot"></i>BRISVALE</div>
    <h1 class="abs headline" style="left:0;top:89px;font-weight:400">YOUR CLEANING IS<br>OUR BUSINESS</h1>
    <svg class="abs" style="left:0;top:0" width="398" height="514" viewBox="0 0 398 514">
      <path d="M240 150 A250 250 0 0 1 398 177" fill="none" stroke="var(--brand)" stroke-width="4"/>
      <path d="M105 514 A255 255 0 0 1 240 150" fill="none" stroke="var(--brand-mid)" stroke-width="4"/>
      <defs><linearGradient id="tower" x1="0" y1="0" x2="0" y2="1"><stop offset="0" stop-color="#e4ecf3"/><stop offset=".6" stroke-color="#9fb0bd" stop-color="#9aaab7"/><stop offset="1" stop-color="#6c7470"/></linearGradient></defs>
      <circle cx="300" cy="400" r="242" fill="url(#tower)" role="img" aria-label="Photo of a modern glass office tower with palm trees at street level"/>
    </svg>
  </article>
</section>

<!-- Cover spread: introduction + services -->
<section class="spread spread--cover">
  <article class="page page--intro">
    <div class="abs wordmark" style="left:23px;top:38px;font-size:27px"><i class="wordmark__dot"></i>BRISVALE</div>
    <h2 class="abs section-title" style="left:23px;top:100px">Your Cleaning is Our Business!</h2>
    <p class="abs body-copy" style="left:23px;top:117px;width:360px">Brisvale, a Janitorial Services Company that has been in business since 1985, takes pride in providing the highest possible quality of janitorial and complete cleaning services for any type/size operation. Brisvale provides services to clients in the GTA, Southern Ontario, and many areas across Canada.</p>
    <ul class="abs values" style="left:23px;top:187px;color:var(--grey)">
      <li><svg style="color:var(--brand-mid)"><use href="#tick-box"/></svg>HEALTH &amp; SAFETY</li>
      <li><svg style="color:var(--brand-mid)"><use href="#tick-box"/></svg>PROFESSIONALISM</li>
      <li><svg style="color:var(--brand-mid)"><use href="#tick-box"/></svg>SECURITY</li>
      <li><svg style="color:var(--brand-mid)"><use href="#tick-box"/></svg>QUALITY CONTROL SYSTEM</li>
    </ul>
    <div class="abs offers" style="left:204px;top:200px">
      <div class="offer">All<br>Estimates<br>FREE</div>
      <div class="offer">New Janitorial<br>Contracts<br>FREE<br><small>Carpet Cleaning</small></div>
      <div class="offer">Janitorial<br>Supplies<br>FREE<br><small>Delivery</small></div>
      <div class="offer">Starting at<br>$95<br><small>Carpet Maintenance<br>Program</small></div>
    </div>
    <svg class="abs" style="left:0;top:0" width="398" height="514" viewBox="0 0 398 514">
      <rect x="0" y="298" width="398" height="216" fill="#1e5aa8"/>
      <path d="M0 295 Q70 268 140 270 Q250 274 290 330 L0 330 Z" fill="#fff"/>
      <path d="M0 292 Q60 266 130 269" fill="none" stroke="var(--brand-mid)" stroke-width="4"/>
      <path d="M0 300 Q140 250 260 320 Q330 370 330 514 L0 514 Z" fill="#c9c6c2" role="img" aria-label="Photo of a cleaning crew in blue shirts mopping and wiping a bright office"/>
      <circle cx="308" cy="450" r="55" fill="var(--brand-mid)"/>
      <circle cx="308" cy="450" r="50" fill="#b8bdc3" role="img" aria-label="Photo of a floor polishing machine on a shiny floor"/>
    </svg>
  </article>

  <article class="page page--services">
    <svg class="abs" style="left:0;top:0" width="398" height="140" viewBox="0 0 398 140">
      <circle cx="313" cy="70" r="90" fill="var(--brand-mid)"/>
      <circle cx="313" cy="68" r="87" fill="#9a9ea4" role="img" aria-label="Photo of a carpet extraction cleaner on grey office carpet"/>
    </svg>
    <h2 class="abs section-title" style="left:20px;top:114px">Other Services</h2>
    <div class="abs other-list" style="left:23px;top:141px;color:var(--brand-mid)">
      <div><svg><use href="#tick-circle"/></svg>Day Porter Services</div>
      <div><svg><use href="#tick-circle"/></svg>Drapery &amp; Blind Cleaning</div>
      <div><svg><use href="#tick-circle"/></svg>Construction Clean-Ups</div>
      <div><svg><use href="#tick-circle"/></svg>Acoustical Tile Cleaning</div>
      <div><svg><use href="#tick-circle"/></svg>Quality Control Inspections</div>
      <div><svg><use href="#tick-circle"/></svg>Computer Terminal, Monitor and Keyboard Cleaning</div>
      <div><svg><use href="#tick-circle"/></svg>Maid Services</div>
      <div><svg><use href="#tick-circle"/></svg>Marble, Granite &amp; Terrazzo Refinishing &amp; Maintenance</div>
      <div><svg><use href="#tick-circle"/></svg>Light &amp; Ceiling Fixture Cleaning</div>
      <div><svg><use href="#tick-circle"/></svg>Power Washing</div>
      <div><svg><use href="#tick-circle"/></svg>Wall Washing</div>
      <div><svg><use href="#tick-circle"/></svg></div>
    </div>

    <div class="abs band"></div>
    <h3 class="abs band-title" style="left:22px;top:315px;font-weight:400">Our Services</h3>
    <div class="abs divider"></div>

    <div class="service" style="left:30px;top:345px"><div class="service__icon" style="left:0;top:0" role="img" aria-label="Janitorial cart icon"></div></div>
    <div class="service" style="left:30px;top:397px">
      <div class="service__icon" style="left:0;top:0" role="img" aria-label="Upholstery cleaning icon"></div>
      <div style="margin-left:36px"><div class="service__title">Carpet &amp; Upholstery Services</div><div class="service__text">Brisvale provides a full upholstery cleaning service.</div></div>
    </div>
    <div class="service" style="left:22px;top:451px">
      <div class="service__icon" style="left:8px;top:0" role="img" aria-label="Restoration cleaning icon"></div>
      <div style="margin-left:44px"><div class="service__title">Fire and Flood Restoration Services</div><div class="service__text">Brisvale provides a full upholstery cleaning service.</div></div>
    </div>
    <div class="service" style="left:228px;top:345px">
      <div class="service__icon" style="left:0;top:0" role="img" aria-label="Cleanroom worker icon"></div>
      <div style="margin-left:36px"><div class="service__title">Cleanroom &amp; GMP services</div><div class="service__text">Brisvale is a leading Cleanroom and GMP services cleaning company with an impressive performance record.</div></div>
    </div>
    <div class="service" style="left:228px;top:397px">
      <div class="service__icon" style="left:0;top:0" role="img" aria-label="Window cleaning icon"></div>
      <div style="margin-left:36px"><div class="service__title">Window Cleaning Services</div><div class="service__text">Brisvale can tackle both high-rise and low level window cleaning.</div></div>
    </div>
    <div class="service" style="left:228px;top:446px">
      <div class="service__icon" style="left:0;top:5px" role="img" aria-label="Cleaning supplies icon"></div>
      <div style="margin-left:36px"><div class="service__title">Sanitation Supplies</div><div class="service__text">Brisvale supplies the highest quality janitorial supplies, contact us for a full list of supplies in stock.</div></div>
    </div>
  </article>
</section>
</body>
</html>
```